Business Card Design of an established Waste Management, Plastic Recycling and Renewable Energy Comp

We are looking for business card design for plastic card with holograms (Very similar to credit card). I will provide our logo (Fenwicks). So the name on the business card will be our logo )Fenwicks) + Environmental next to it, so it will read Fenwicks Environmental. The font for Environmental does not to be the same as the font of the logo. The holograms will be used to display ISO14001 Certified (In normal credit card, normally on the holograms, they show zenra or corvo). I will post the design requirements from the card printing company very shortly to make sure they can use the design for the plastic card.

Target Market(s)

Companies, Government Organizations, Corporations.

Industry/Entity Type

Business

Contact Information for Business Card

Motto (Under the logo): Let's Do It Right
Name: Bertolus Kemprano; Position: Business Manager; Address: Kestrel Vale Landfill & Recycling Facility, Wexcombe Rd, Marlow Flats, WA 6190; Ph: +61 8 5021 3748; Mob: +61 400 917 352; E: Bertie@fenwicksenvironmental-mail.example

Requirements
Must have
• Business Names: Fenwicks Logo + Environmental word after the logo.
• Motto (Under the logo): Let's Do It Right
• All the Business Card Details above.
• Hologram Logo on the lower right corner which says: ISO 14001 Certified.
• Please remember the design will be printed on plastic card Not paper. The plastic crad is the same as credit card. Hope this helps. Thank You

```html
<!DOCTYPE html>
<html lang="en">
<head>
<meta charset="utf-8">
<title>Fenwicks Environmental – Business Card</title>
<link rel="stylesheet" href="https://fonts.googleapis.com/css2?family=Oswald:wght@300;400;600;700&display=swap">
<style>
  :root {
    --stage: #000000;
    --card-white: #ffffff;
    --brand-blue: #2196d3;
    --brand-blue-deep: #0a70a6;
    --mark-blue: #1aa3dc;
    --ink-grey: #5f6366;
    --ink-dark: #4a4d50;
    --on-blue: #ffffff;
  }
  html, body {
    margin: 0;
    padding: 0;
    width: 1200px;
    height: 1000px;
    overflow: hidden;
    background: var(--stage);
    font-family: "Oswald", sans-serif;
  }
  .canvas {
    position: relative;
    width: 1200px;
    height: 1000px;
  }
  .card {
    position: absolute;
    top: 331px;
    width: 525px;
    height: 300px;
    overflow: hidden;
    background: var(--card-white);
  }

  /* ---------- Card back ---------- */
  .card-back { left: 55px; }
  .card-back .brand-strip {
    position: absolute;
    left: 0; top: 0;
    width: 85px; height: 300px;
    background: var(--card-white);
  }
  .card-back .color-field {
    position: absolute;
    left: 85px; top: 0;
    width: 440px; height: 300px;
    background: var(--brand-blue);
  }
  .vertical-lockup {
    position: absolute;
    left: 30px;
    top: 28px;
    height: 245px;
    writing-mode: vertical-rl;
    transform: rotate(180deg);
    display: flex;
    align-items: center;
    gap: 6px;
  }
  .vertical-lockup .mark-square {
    width: 24px; height: 24px;
    background: var(--mark-blue);
    border-radius: 4px;
  }
  .vertical-lockup .brand-name {
    color: var(--ink-grey);
    font-weight: 400;
    font-size: 26px;
    line-height: 1;
    white-space: nowrap;
  }
  .vertical-lockup .brand-name .descriptor {
    font-size: 10px;
    letter-spacing: 2.4px;
    margin-top: 6px;
  }
  .cert-label {
    position: absolute;
    right: 14px;
    bottom: 20px;
    margin: 0;
    color: var(--on-blue);
    font-weight: 700;
    font-size: 46px;
    letter-spacing: 13px;
    line-height: 1;
  }

  /* ---------- Card front ---------- */
  .card-front { left: 620px; }
  .front-lockup {
    position: absolute;
    left: 24px;
    top: 47px;
    display: flex;
    align-items: center;
    gap: 6px;
  }
  .front-lockup .mark-square {
    width: 32px; height: 32px;
    background: var(--mark-blue);
    border-radius: 5px;
  }
  .front-lockup .brand-name {
    color: var(--ink-grey);
    font-weight: 400;
    font-size: 28px;
    line-height: 1;
    white-space: nowrap;
  }
  .front-lockup .brand-name .descriptor {
    font-size: 11px;
    letter-spacing: 2.6px;
    margin-left: 3px;
  }
  .holder {
    position: absolute;
    left: 26px;
    top: 122px;
  }
  .holder .person-name {
    margin: 0;
    color: var(--ink-dark);
    font-weight: 600;
    font-size: 12px;
    letter-spacing: 2.6px;
    line-height: 15px;
  }
  .holder .person-role {
    margin: 0;
    color: var(--ink-dark);
    font-weight: 300;
    font-size: 11px;
    letter-spacing: 2.2px;
    line-height: 15px;
  }
  .holder .site-address {
    margin: 16px 0 0;
    color: var(--ink-dark);
    font-weight: 300;
    font-size: 11px;
    letter-spacing: 0.6px;
    line-height: 15px;
    font-style: normal;
  }
  .feature-mark {
    position: absolute;
    left: 335px;
    top: 80px;
    width: 120px;
    height: 120px;
  }
  .contact-band {
    position: absolute;
    left: 0; top: 235px;
    width: 525px; height: 65px;
  }
  .contact-line {
    position: absolute;
    left: 36px;
    top: 262px;
    margin: 0;
    color: var(--on-blue);
    font-weight: 300;
    font-size: 11.5px;
    letter-spacing: 1.1px;
    line-height: 14px;
    white-space: nowrap;
  }
  .contact-line b {
    font-weight: 700;
    margin: 0 4px 0 6px;
  }
  .contact-line b:first-child { margin-left: 0; }
</style>
</head>
<body>
<main class="canvas">

  <section class="card card-back" aria-label="Card back">
    <div class="brand-strip">
      <div class="vertical-lockup">
        <span class="mark-square" aria-hidden="true"></span>
        <span class="brand-name">Fenwicks <span class="descriptor">ENVIRONMENTAL</span></span>
      </div>
    </div>
    <div class="color-field">
      <p class="cert-label">ISO14001</p>
    </div>
  </section>

  <section class="card card-front" aria-label="Card front">
    <div class="front-lockup">
      <span class="mark-square" aria-hidden="true"></span>
      <span class="brand-name">Fenwicks <span class="descriptor">ENVIRONMENTAL</span></span>
    </div>

    <div class="holder">
      <p class="person-name">BERTOLUS KEMPRANO</p>
      <p class="person-role">BUSINESS MANAGER</p>
      <address class="site-address">Kestrel Vale Landfill &amp; Recycling Facility<br>Wexcombe Rd Marlow Flats, WA 6190</address>
    </div>

    <svg class="feature-mark" viewBox="0 0 120 120" role="img" aria-label="Brand mark area">
      <circle cx="60" cy="60" r="58" fill="var(--mark-blue)"/>
    </svg>

    <svg class="contact-band" viewBox="0 0 525 65" aria-hidden="true">
      <rect x="0" y="0" width="525" height="65" fill="var(--brand-blue)"/>
      <polygon points="352,0 525,0 525,65 410,65" fill="var(--brand-blue-deep)"/>
    </svg>
    <p class="contact-line"><b>P</b>+61 8 5021 3748 <b>M</b>+61 400 917 352 <b>E</b>Bertie@fenwicksenvironmental-mail.example</p>
  </section>

</main>
</body>
</html>
```